Bluegull Harbor Tours and Charters

I'm looking to update my current website that was written in Joomla. I would like to move to a more modern design that works well on all platforms using a Wordpress theme. The website is, https://www.bluegullharbortours.example/ It should be noted that I currently have an online booking API (Tidebook) that is integrated with the site but I don't want to worry about that for now. Once I get the new site up and running I am going to move to Quayly which doesn't hook into the site, it just links to an external booking company. Just ignore the Tidebook booking (Book Now) code and build the site. IMPORTANT: My website is hosted on HostMarlow and I currently manage it through cPanel. I want to be able to make changes, updates and manage the website once its completed.

Target Market(s)

Tourists visiting Siesta Key and Venice Florida for Dolphin, sunset tours and private half and full day charters to Pelican Rib Island.

Industry/Entity Type

Tourism

Coding

Coded - Design and coding required

Font styles to use
Other font styles liked:
• Freebooter

Colors
0455a3
85acd3
fbed22
fbee3e
ffc214
ffcf3e
f78f20
faa54b

Requirements
Must have
• Our brand is fun on the water. Social Media links. Great photos, we will provide, and compelling descriptions of each of the tours we offer.
• Dolphin Tours
• Sunset Tours
• Shelling and Snorkeling
• Boating Instruction - I would like this page to have a more professional look and feel. It needs to stand out from the other pages as a professional service yet it still needs to blend well with the entire site.
• What can you do to make this site, https://www.bluegullharbortours.example/ better?
• I don't really need a "Gallery Page" but I want to highlight lots of great pics from our tours. Here is a good example..... check this site out.
• https://brindlecharters.example/
• I don't want to be "like" Brindle Charters, I want my site to be better. This is my competitor.
Nice to have
• I selected some colors for the theme but basically I just want it to be a bright, fun and outgoing site.
• There is a font you can download called Freebooter. It gives it that Pirate look and feel. I would like to use that in some places. Its in my logo on the website. Don't go overboard with the Pirate look and feel but some subtitle pirate things in the site would make it fun.

```html
<!DOCTYPE html>
<html lang="en">
<head>
<meta charset="utf-8">
<title>Bluegull Harbor Tours and Charters</title>
<link rel="stylesheet" href="https://fonts.googleapis.com/css2?family=Great+Vibes&family=Montserrat:wght@400;500;600&family=Playfair+Display:wght@700&display=swap">
<style>
:root{
  --blue:#1c3fa6;
  --blue-deep:#0b2a86;
  --blue-mid:#1f55c4;
  --sky:#85acd3;
  --yellow:#f8d24c;
  --yellow-soft:#fbe07a;
  --button:#f5c214;
  --orange:#f78f20;
  --ink:#2a2a2a;
  --white:#ffffff;
  --serif:"Playfair Display", Georgia, serif;
  --sans:"Montserrat", Arial, sans-serif;
  --script:"Great Vibes", cursive;
}
*{box-sizing:border-box;margin:0;padding:0}
html,body{width:1200px;height:4813px;overflow:hidden}
body{font-family:var(--sans);color:var(--ink);background:var(--white);position:relative}
.abs{position:absolute}
.btn{display:inline-block;background:var(--button);color:#222;font:600 13px var(--sans);text-transform:uppercase;padding:12px 30px;letter-spacing:.5px}
.h-serif{font-family:var(--serif);color:var(--blue);text-transform:uppercase;font-weight:700}

/* hero */
.hero{top:0;left:0;width:1200px;height:865px;background:linear-gradient(180deg,#3a4a6a 0%,#7a6a70 30%,#d28a4a 52%,#3d4c78 62%,#1d2d5a 100%)}
.brand{top:0;left:497px;width:206px;height:128px;background:var(--white);display:flex;flex-direction:column;align-items:center;justify-content:center;gap:8px}
.brand .dot{width:34px;height:34px;border-radius:50%;background:var(--orange)}
.brand span{font:600 14px var(--sans);color:var(--blue);text-align:center;line-height:1.2}
.nav{top:200px;left:90px;width:1020px;height:58px;background:var(--white);display:flex}
.nav a{font:500 15px var(--sans);color:#333;text-decoration:none;display:flex;align-items:center;padding:0 30px}
.nav a.active{background:#f6a623;color:var(--white)}
.hero-tag{top:580px;width:1200px;text-align:center;font:64px var(--script);color:#f6c24a}
.hero-title{top:650px;width:1200px;text-align:center;font:400 62px Georgia,serif;color:var(--white);font-family:"Playfair Display",serif;font-weight:400}
.anchor-deco{top:690px;left:940px;width:140px;height:170px;border-radius:8px;background:linear-gradient(160deg,#d9d2c2,#8d8470);opacity:.75}

/* tours intro */
.intro{top:865px;left:0;width:1200px;height:895px;background:var(--yellow)}
.intro h2{position:absolute;top:75px;width:1200px;text-align:center;font-size:27px}
.intro .lead{position:absolute;top:130px;left:170px;width:860px;text-align:center;font-size:12.5px;line-height:1.55}
.intro .lead p{margin-bottom:8px}
.card{position:absolute;top:323px;width:334px;height:468px;background:var(--white);box-shadow:0 6px 18px rgba(0,0,0,.18);text-align:center;padding:22px}
.card .photo{height:190px}
.card h3{margin:36px 0 12px;font-size:24px;line-height:1.1}
.card p{font-size:12.5px;line-height:1.5;padding:0 20px}
.card .btn{margin-top:18px}

/* charter */
.charter-photo{top:1830px;left:45px;width:648px;height:410px;background:linear-gradient(135deg,#8fb6d8,#3f6b9e 60%,#d7e6f2)}
.charter-text{top:1900px;left:738px;width:425px}
.charter-text h2{font-size:28px}
.charter-text .sub{color:#e6a81a;font-size:15px;margin:16px 0 14px}
.charter-text p{font-size:13px;line-height:1.6;color:#444}
.charter-text .btn{margin-top:28px}

/* video */
.video{top:2295px;left:0;width:1200px;height:915px;background:linear-gradient(180deg,#ffffff 0%,#ffffff 8%,#2a62d0 14%,#1b47b4 45%,#0b2a86 100%)}
.video .dolphins{position:absolute;top:10px;left:0;width:1200px;height:110px}
.video h2{position:absolute;top:140px;width:1200px;text-align:center;font:400 32px var(--serif);color:var(--white)}
.video-frame{top:311px;left:138px;width:937px;height:514px;background:linear-gradient(180deg,#8ec0ec 0%,#cfe3f4 40%,#3fa3c2 70%,#1f6f95 100%);box-shadow:0 10px 24px rgba(0,0,0,.35)}
.play{top:212px;left:418px;width:100px;height:100px}

/* tours list */
.tours{top:3210px;left:0;width:1200px;height:930px}
.tours h2{position:absolute;top:50px;width:1200px;text-align:center;font-size:27px}
.tours .lead{position:absolute;top:100px;left:170px;width:860px;text-align:center;font-size:13px;line-height:1.6}
.tour{position:absolute;width:500px;display:flex;gap:26px}
.tour .thumb{width:167px;height:162px;flex:none;border:6px solid #eee}
.tour h3{font-size:21px;line-height:1.15;margin-top:8px}
.tour p{font-size:12.5px;line-height:1.5;margin:12px 0}
.tour .price{color:#e6a81a;font-size:14px;margin-bottom:14px}
.tour .price small{color:#555}

/* gallery */
.gallery{top:4140px;left:0;width:1200px;height:212px;display:flex;gap:8px;padding:0 14px}
.gallery div{flex:1}
.arrow{top:4230px;width:34px;height:34px;background:var(--button)}

/* footer */
.footer{top:4430px;left:0;width:1200px;height:383px;background:linear-gradient(180deg,#2a62d0 0%,#12349c 30%,#0a2273 100%);color:var(--white)}
.footer .col{position:absolute;top:144px;text-align:center}
.footer h4{font:700 15px var(--serif);color:#f6c24a;text-transform:uppercase;margin-bottom:14px}
.footer .col span{font-size:15px}
.footer .copy{position:absolute;top:318px;left:60px;font-size:12px}
.footer .follow{position:absolute;top:312px;right:70px;display:flex;align-items:center;gap:12px;font:700 15px var(--serif);color:#f6c24a}
.footer .follow i{width:36px;height:36px;border-radius:50%;background:var(--white);display:block}
</style>
</head>
<body>

<section class="abs hero">
  <div class="abs brand"><i class="dot"></i><span>Bluegull Harbor Tours<br>and Charters</span></div>
  <nav class="abs nav">
    <a class="active">Home</a><a>Dolphin Tours</a><a>Sunset Tour</a><a>Shelling and Snorkeling</a><a>Boating Instruction</a><a>Contact us</a>
  </nav>
  <div class="abs hero-tag">let's feel</div>
  <h1 class="abs hero-title">Cruise Experience</h1>
  <div class="abs anchor-deco" role="img" aria-label="Decorative ship anchor with rope"></div>
</section>

<section class="abs intro">
  <h2 class="h-serif">Dolphin, Sightseeing &amp; Sunset Tours!</h2>
  <div class="lead">
    <p>Our goal is for you to have your best vacation day ever, so let us help plan your adventure. We offer sightseeing tours, charters, boat rides or special event services. It's your adventure, relax and let us take you there. No matter what you decide, you will have a great time aboard our brand new comfortable 23 foot boat. We promise you'll see tons of wild life and enjoy breathtaking views of the inland waterways and the Gulf.</p>
    <p>Our waterways are home to dolphin, manatee, bald eagles, osprey, stingrays, spotted eagle rays, sea turtles and so much more. There are islands, sand bars and keys to explore, tiki bars and restaurants to visit and we'll take you to places you can only visit by boat!</p>
    <p>Whether you are with us for a few hours or a full day, we promise you'll have no worries with Bluegull Harbor Tours and Charters. Our boats are equipped with everything you will need for your trip and we do all of the work so you can relax and just make great memories.</p>
  </div>
  <article class="card" style="left:77px">
    <div class="photo" role="img" aria-label="Dolphin surfacing in blue water" style="background:linear-gradient(180deg,#4aa3c9,#1e6b95)"></div>
    <h3 class="h-serif">Dolphin Tours</h3>
    <p>Maecenas augue nibh, congue ut ante id, tempus vestibulum sem. Praesent interdum leo sit amet sapien porta interdum.</p>
    <span class="btn">Read more</span>
  </article>
  <article class="card" style="left:437px">
    <div class="photo" role="img" aria-label="Orange sunset over the Gulf" style="background:linear-gradient(180deg,#f0a24a,#c0622a 55%,#3b3d55)"></div>
    <h3 class="h-serif">Sunset Tours</h3>
    <p>Quisque eu dolor tempus mi fermentum fermentum. Vestibulum ante ipsum primis in faucibus orci luctus.</p>
    <span class="btn">Read more</span>
  </article>
  <article class="card" style="left:796px">
    <div class="photo" role="img" aria-label="Seashell resting on white sand" style="background:linear-gradient(180deg,#e4e1da,#b8ada0)"></div>
    <h3 class="h-serif">Shelling and Snorkelling</h3>
    <p>Nulla eu lacus mattis, eleifend tortor at, tincidunt neque. Donec dolor lorem, rutrum eu ipsum quis, venenatis finibus eros.</p>
    <span class="btn">Read more</span>
  </article>
</section>

<div class="abs charter-photo" role="img" aria-label="Group of guests smiling on the boat deck with wake behind"></div>
<div class="abs charter-text">
  <h2 class="h-serif">The Best Charter. Period.</h2>
  <p class="sub">Why Should You Choose Bluegull Harbor Tours?</p>
  <p>This is not just a job to us. This is a business and a lifestyle we are passionate about, and are truly excited to share. Our approach is genuine, honest and always positive while connecting with people is our forte; this is not just a job to us. This is a business and a lifestyle we are passionate about, and are truly excited to share. Our approach is genuine, honest and always positive.</p>
  <span class="btn">Read more</span>
</div>

<section class="abs video">
  <svg class="dolphins" viewBox="0 0 1200 110" role="img" aria-label="Dolphins leaping above waves">
    <path d="M0 80 Q150 60 300 78 T600 76 T900 80 T1200 74 V110 H0Z" fill="#2a62d0"/>
  </svg>
  <h2>WATCH OUR VIDEO</h2>
  <div class="abs video-frame" role="img" aria-label="Tour boat on the water with a dolphin alongside">
    <svg class="abs play" viewBox="0 0 100 100"><circle cx="50" cy="50" r="48" fill="#fff"/><circle cx="50" cy="50" r="40" fill="#0b2a86"/><path d="M42 34 L68 50 L42 66Z" fill="#fff"/></svg>
  </div>
</section>

<section class="abs tours">
  <h2 class="h-serif">Tours and Charters</h2>
  <p class="lead">Whether you are with us for a few hours or a full day, we promise you'll have no worries with Bluegull Harbor Tours and Charters. You will be impressed with our outstanding service. With Bluegull Harbor Tours, we handle all of the details.</p>
  <div class="tour" style="left:77px;top:218px">
    <div class="thumb" role="img" aria-label="Harbor view with boats" style="background:linear-gradient(180deg,#a9c8e2,#5a7d95)"></div>
    <div><h3 class="h-serif">Sunset Tours (Approximately 2 Hours)</h3><p>Maecenas augue nibh, congue ut ante id, tempus vestibulum sem. Praesent interdum leo sit amet sapien porta interdum.</p><div class="price">$40 <small>/ person</small></div><span class="btn">Read more</span></div>
  </div>
  <div class="tour" style="left:616px;top:218px">
    <div class="thumb" role="img" aria-label="Waterfront town skyline" style="background:linear-gradient(180deg,#b8cde0,#6d7f8c)"></div>
    <div><h3 class="h-serif">Sunset Tours (Approximately 2 Hours)</h3><p>Quisque eu dolor tempus mi fermentum fermentum. Vestibulum ante ipsum primis in faucibus orci luctus.</p><div class="price">$40 <small>/ person</small></div><span class="btn">Read more</span></div>
  </div>
  <div class="tour" style="left:77px;top:562px">
    <div class="thumb" role="img" aria-label="Coastal village on a hillside" style="background:linear-gradient(180deg,#9cc1de,#c29a72)"></div>
    <div><h3 class="h-serif">Custom Destination Charters</h3><p>Nulla eu lacus mattis, eleifend tortor at, tincidunt neque. Donec dolor lorem, rutrum eu ipsum quis, venenatis.</p><div class="price">$40 <small>/ person</small></div><span class="btn">Read more</span></div>
  </div>
  <div class="tour" style="left:616px;top:562px">
    <div class="thumb" role="img" aria-label="River winding through green hills" style="background:linear-gradient(180deg,#a8c4d8,#5b7a5a)"></div>
    <div><h3 class="h-serif">Sunset Tours (Approximately 2 Hours)</h3><p>Sed a ornare dolor, ac aliquam ipsum. Aliquam dignissim ut lorem eget tristique. Vestibulum ut sem urna.</p><div class="price">$40 <small>/ person</small></div><span class="btn">Read more</span></div>
  </div>
</section>

<div class="abs gallery">
  <div role="img" aria-label="Guest on a boat" style="background:linear-gradient(180deg,#7fa7c9,#3c5d7c)"></div>
  <div role="img" aria-label="Dolphin jumping near the boat" style="background:linear-gradient(180deg,#9bc0dc,#2f6f95)"></div>
  <div role="img" aria-label="Calm open water" style="background:linear-gradient(180deg,#bcd6ea,#4f8fb8)"></div>
  <div role="img" aria-label="Children holding shells" style="background:linear-gradient(180deg,#8fbddc,#c9a98a)"></div>
  <div role="img" aria-label="Family on the beach" style="background:linear-gradient(180deg,#a9cbe6,#8c7f6a)"></div>
</div>
<svg class="abs arrow" style="left:14px" viewBox="0 0 34 34"><rect width="34" height="34" fill="#f5c214"/><path d="M20 10 L13 17 L20 24" stroke="#222" stroke-width="3" fill="none"/></svg>
<svg class="abs arrow" style="left:1152px" viewBox="0 0 34 34"><rect width="34" height="34" fill="#f5c214"/><path d="M14 10 L21 17 L14 24" stroke="#222" stroke-width="3" fill="none"/></svg>

<footer class="abs footer">
  <div class="col" style="left:80px;width:230px"><h4>Gift Cards Available</h4><span>Purchase Today</span></div>
  <div class="col" style="left:430px;width:200px"><h4>Phone</h4><span>941.555.0147</span></div>
  <div class="col" style="left:780px;width:370px"><h4>Email</h4><span>info@bluegullharbortours.example</span></div>
  <p class="copy">Copyright © 2019 Bluegull Harbor Tours. Privacy Policy &amp; Cookie Policy.</p>
  <div class="follow">Follow us on : <i></i></div>
</footer>

</body>
</html>
```